Pembrook Nightclub Flyer Grand Opening

Grand Opening Teaser Flyer For Nightclub

Text for flyer:
PEMBROOK
Nightclub + Lounge
Opening Fall 2018
Downtown Sacramento
Now Hiring (All Positions)
www.pembrookvenue.example
Powered by HALM Acoustics

Email Resume to: club@pembrookvenue.example

Target Market(s)

Upscale Nightclub and Lounge

Industry/Entity Type

Night Club

Font styles to use
Sans Serif

Colors
9ccb3b
0393ce
0355a3
b2b2b2
000000

Requirements
Must have
• Vibrant colors like the flyer example, and our logo. For use on Circlebook and Snapgrid, will be boosted as well.
Nice to have
• Something artsy like the flyer example but not required

```html
<!DOCTYPE html>
<html lang="en">
<head>
<meta charset="utf-8">
<title>Pembrook Nightclub – Grand Opening Social Ads</title>
<link rel="stylesheet" href="https://fonts.googleapis.com/css2?family=Montserrat:ital,wght@0,400;0,500;0,600;0,700;1,400&display=swap">
<style>
  :root {
    --board-light: #ffffff;
    --board-edge: #cfd2d6;
    --label-grey: #b2b2b2;
    --night: #000000;
    --deep-blue: #0355a3;
    --electric-blue: #0393ce;
    --ice: #bfe9ff;
    --mint: #8cf0bd;
    --lime: #9ccb3b;
    --white: #ffffff;
  }
  * { box-sizing: border-box; margin: 0; padding: 0; }
  html, body { width: 1200px; height: 923px; overflow: hidden; }
  body {
    position: relative;
    font-family: "Montserrat", sans-serif;
    background: radial-gradient(ellipse at 50% 45%, var(--board-light) 40%, var(--board-edge) 100%);
  }

  .ad {
    position: absolute;
    overflow: hidden;
    background: var(--night);
    color: var(--white);
  }
  .ad--square { left: 45px; top: 150px; width: 580px; height: 579px; }
  .ad--landscape { left: 643px; top: 221px; width: 515px; height: 435px; }

  .ad__artwork {
    position: absolute; inset: 0;
    background:
      radial-gradient(ellipse at 50% 30%, rgba(3,147,206,0.85) 0%, rgba(3,85,163,0.6) 35%, transparent 70%),
      radial-gradient(ellipse at 20% 80%, rgba(3,85,163,0.9) 0%, transparent 55%),
      radial-gradient(ellipse at 85% 75%, rgba(3,147,206,0.7) 0%, transparent 50%),
      linear-gradient(180deg, #02102a 0%, #031a55 45%, #0a2bb0 70%, #020614 100%);
  }

  .ad__line {
    position: absolute; left: 0; right: 0;
    text-align: center; white-space: nowrap;
    transform: translateY(-50%);
  }
  .ad__name { color: var(--mint); font-weight: 600; }
  .ad__subtitle { color: var(--white); font-weight: 600; }
  .ad__location { color: var(--mint); font-weight: 500; }
  .ad__hiring { color: var(--white); font-weight: 500; }
  .ad__url { color: var(--white); font-weight: 700; }

  .ad__contact { position: absolute; font-style: italic; color: var(--white); letter-spacing: 0.03em; }
  .ad__sponsor { position: absolute; text-align: center; color: var(--ice); }
  .sponsor__lead { display: block; font-weight: 500; }
  .sponsor__name { display: block; font-weight: 700; line-height: 1; }
  .sponsor__kind { display: block; letter-spacing: 0.4em; }

  .stamp {
    position: absolute; border-radius: 50%;
    border: 2px solid var(--white);
    display: flex; flex-direction: column; align-items: center; justify-content: center;
    transform: translate(-50%, -50%) rotate(-22deg);
    font-weight: 700; line-height: 1.05; color: var(--white);
  }

  /* Square feed sizing */
  .ad--square .stamp { left: 86px; top: 65px; width: 112px; height: 112px; font-size: 17px; }
  .ad--square .stamp__year { font-size: 22px; }
  .ad--square .ad__name { top: 192px; font-size: 54px; letter-spacing: 26px; padding-left: 26px; }
  .ad--square .ad__subtitle { top: 243px; font-size: 24px; letter-spacing: 14px; padding-left: 14px; }
  .ad--square .ad__location { top: 315px; font-size: 25px; }
  .ad--square .ad__hiring { top: 402px; font-size: 25px; }
  .ad--square .ad__url { top: 447px; font-size: 19px; }
  .ad--square .ad__contact { left: 25px; top: 498px; font-size: 18px; line-height: 26px; }
  .ad--square .ad__sponsor { right: 25px; top: 484px; }
  .ad--square .sponsor__lead { font-size: 15px; }
  .ad--square .sponsor__name { font-size: 40px; }
  .ad--square .sponsor__kind { font-size: 13px; }

  /* Landscape feed sizing */
  .ad--landscape .stamp { left: 55px; top: 46px; width: 84px; height: 84px; font-size: 13px; }
  .ad--landscape .stamp__year { font-size: 16px; }
  .ad--landscape .ad__name { top: 145px; font-size: 44px; letter-spacing: 20px; padding-left: 20px; }
  .ad--landscape .ad__subtitle { top: 181px; font-size: 20px; letter-spacing: 12px; padding-left: 12px; }
  .ad--landscape .ad__location { top: 236px; font-size: 18px; }
  .ad--landscape .ad__hiring { top: 317px; font-size: 19px; }
  .ad--landscape .ad__url { top: 350px; font-size: 15px; }
  .ad--landscape .ad__contact { left: 20px; top: 372px; font-size: 15px; line-height: 21px; }
  .ad--landscape .ad__sponsor { right: 21px; top: 362px; }
  .ad--landscape .sponsor__lead { font-size: 11px; }
  .ad--landscape .sponsor__name { font-size: 30px; }
  .ad--landscape .sponsor__kind { font-size: 10px; }

  .format-label {
    position: absolute;
    color: var(--label-grey);
    font-weight: 600;
    font-size: 27px;
    white-space: nowrap;
  }
  .format-label--square { left: 44px; top: 731px; }
  .format-label--landscape { left: 644px; top: 661px; }
</style>
</head>
<body>

  <section class="ad ad--square">
    <div class="ad__artwork" role="img" aria-label="Electric blue lightning, sound-wave and equaliser artwork with the silhouette of a dancer"></div>
    <div class="stamp"><span>OPENING</span><span>FALL</span><span class="stamp__year">2018</span></div>
    <div class="ad__line ad__name">PEMBROOK</div>
    <div class="ad__line ad__subtitle">NIGHTCLUB &amp; LOUNGE</div>
    <div class="ad__line ad__location">DOWNTOWN SACRAMENTO</div>
    <div class="ad__line ad__hiring">NOW HIRING (ALL POSITIONS)</div>
    <div class="ad__line ad__url">WWW.PEMBROOKVENUE.EXAMPLE</div>
    <p class="ad__contact">e-mail resume to:<br>club@pembrookvenue.example</p>
    <div class="ad__sponsor">
      <span class="sponsor__lead">Powered by</span>
      <span class="sponsor__name">HALM</span>
      <span class="sponsor__kind">ACOUSTICS</span>
    </div>
  </section>

  <section class="ad ad--landscape">
    <div class="ad__artwork" role="img" aria-label="Electric blue lightning, sound-wave and equaliser artwork with the silhouette of a dancer"></div>
    <div class="stamp"><span>OPENING</span><span>FALL</span><span class="stamp__year">2018</span></div>
    <div class="ad__line ad__name">PEMBROOK</div>
    <div class="ad__line ad__subtitle">NIGHTCLUB &amp; LOUNGE</div>
    <div class="ad__line ad__location">DOWNTOWN SACRAMENTO</div>
    <div class="ad__line ad__hiring">NOW HIRING (ALL POSITIONS)</div>
    <div class="ad__line ad__url">WWW.PEMBROOKVENUE.EXAMPLE</div>
    <p class="ad__contact">e-mail resume to:<br>club@pembrookvenue.example</p>
    <div class="ad__sponsor">
      <span class="sponsor__lead">Powered by</span>
      <span class="sponsor__name">HALM</span>
      <span class="sponsor__kind">ACOUSTICS</span>
    </div>
  </section>

  <p class="format-label format-label--square">Snapgrid Ad - 1080x1080</p>
  <p class="format-label format-label--landscape">Circlebook Ad - 960x810</p>

</body>
</html>
```